COMPETITION TITLE:
Premium Skincare Packaging Design for Modern Hydration Beauty Brand
ABOUT THE PROJECT
We are developing a new skincare brand called VELORIQUE.
We are looking for a sophisticated and commercially strong packaging design direction for our initial skincare soft launch.
The brand positioning is:
* modern premium skincare
* hydration-focused
* wellness-oriented
* calming and elegant
* emotionally reassuring
* modern feminine skincare
* premium online beauty brand
The products are designed around hydration, skin comfort and modern skincare rituals.
The brand is inspired by modern hydration and skin wellness for people adapting between warmer and colder climates. The visual direction should therefore feel emotionally warm, comforting and restorative while remaining modern, refined and internationally premium rather than overtly cultural or decorative.
WHAT WE NEED
We are primarily seeking the VISUAL DIRECTION and PACKAGING IDENTITY for one hero product:
LIGHT MOISTURISING DAY CREAM
The winning visual direction will later be adapted across additional products within the range, including:
* Brightening Eye Cream
* Hydrating Mist / Toner
Therefore we are looking for a cohesive skincare brand identity system rather than unrelated individual designs.
IMPORTANT PACKAGING INFORMATION
The product packaging is:
* white plastic pump dispenser bottle
* transparent clear plastic lid
* outer cardboard carton/box
Bottle dimensions:
* diameter: 30mm
* total height including lid: 147mm
* bottle body height: approx. 120mm
* transparent lid height: approx. 27mm
Outer carton dimensions:
* height: 150mm
* width: 40mm x 35mm
IMPORTANT:
The packaging itself is minimalist and lightweight, therefore the LABEL DESIGN and OVERALL BRAND DIRECTION should visually elevate the product and make it feel:
* premium
* substantial
* calming
* elegant
* modern
* trustworthy
* emotionally warm
* intentional
The design should help the packaging feel significantly more premium than standard mass-market skincare.
FILES PROVIDED
We are providing:
* bottle label template
* outer box template
* logo/icon
* packaging dimensions
The supplied logo/icon should be retained conceptually, however designers may professionally refine and recreate/vectorise the artwork where required for packaging consistency and premium presentation.
At this stage we are NOT looking for final technical production artwork.
We are primarily looking for:
* visual direction
* typography
* colour palette
* premium skincare aesthetic
* realistic product mockups
IMPORTANT WEBSITE NOTE
A current website link may be provided for background information only.
Please DO NOT take heavy visual inspiration from the existing website design, as the website itself is expected to evolve in the future alongside the packaging direction.
The packaging design should therefore LEAD the future visual identity of the brand rather than follow the current website styling.
DESIGN STYLE
We are looking for:
* modern premium wellness skincare
* understated luxury
* elegant typography
* emotionally warm but clean branding
* hydration-focused beauty aesthetic
* premium online skincare look
The product should feel:
* calming when held
* emotionally reassuring rather than clinical
* modern wellness rather than minimalist pharmacy
* elegant but human rather than cold luxury
* comforting and restorative rather than cosmetic-only
Subtle texture, tonal layering and sophisticated visual depth are encouraged where appropriate.
Designers are encouraged to create a recognisable and distinctive visual identity rather than generic minimalist skincare packaging.
PLEASE AVOID
* gold luxury clichés
* ornate decorative themes
* floral overload
* influencer-style beauty branding
* overly clinical pharmacy aesthetics
* generic Plindo-style layouts
* packaging that feels cold or sterile
STYLE REFERENCES
Please take inspiration from brands such as:
* Mirova
* Bright Petal
* Coravel
* Grace of Kellmar
We particularly like:
* elegant spacing
* clean premium typography
* calm colour palettes
* subtle luxury
* modern hydration skincare aesthetics
COLOUR DIRECTION
Preferred tones include:
* warm ivory
* soft cream
* muted blush
* sand
* charcoal typography
* subtle deep plum accents
* restrained muted rose-gold accents
Please avoid:
* neon colours
* excessive metallic effects
* harsh black-and-white pharmacy styling
* very dark packaging
IMPORTANT DESIGN NOTE
The slim vertical packaging should feel intentionally elegant and premium rather than small or sample-sized.
The label design should visually elongate and elevate the packaging.
LOGO
An existing logo/icon is provided and should be retained and integrated into the design direction rather than completely redesigned.
DELIVERABLES
We are looking for:
* one fully developed hero product design
* realistic bottle + outer box mockups
* coordinated visual direction suitable for future product extensions
* typography and colour direction
* editable source files
The final approved visual system will later be adapted across additional products within the range.
BRAND NAME
VELORIQUE
OPTIONAL TAGLINE DIRECTION
Climate Adapt Hydration
Updates
Thank you everyone for the submissions so far — there are some very strong directions emerging.
A few important thoughts as the project develops:
We are looking not only for attractive skincare labels, but for a distinctive and recognisable BRAND IDENTITY that could grow with the business over time across future packaging formats including larger cartons, jars and premium skincare packaging.
One area we would particularly encourage designers to explore further is refinement/elevation of the existing logo/icon. We would like to retain the core rose/circle concept, however subtle refinement, balance, geometry, typography pairing and premium presentation are encouraged where appropriate.
The strongest directions for us so far are those that feel:
* emotionally warm rather than clinical
* modern premium wellness rather than generic minimal skincare
* calming and reassuring when viewed or held
* elegant and distinctive rather than trend-driven
* premium without relying on gold luxury clichés
We are especially interested in designs that create a memorable visual identity system rather than simply placing text onto a white skincare bottle.
Subtle tonal layering, refined typography, understated sophistication and intelligent visual restraint are all encouraged.
Many thanks again and we are very excited to see the next round of directions develop.

```html
<!DOCTYPE html>
<html lang="en">
<head>
<meta charset="utf-8">
<title>VELORIQUE – Light Moisturising Cream Packaging</title>
<link href="https://fonts.googleapis.com/css2?family=Barlow+Semi+Condensed:wght@300;400&display=swap" rel="stylesheet">
<style>
  :root {
    --backdrop: #f7efe6;
    --pack-white: #fbfbf8;
    --pack-edge: #ecece6;
    --cap-clear: rgba(240, 244, 240, 0.55);
    --cap-edge: #dfe3dc;
    --pump-sage: #cfdcc4;
    --label-sage: #e2e9d2;
    --block-sage: #959e89;
    --leaf-tone: #cdd6bd;
    --type-light: #f3f5ec;
    --badge-tone: #a3ab98;
    --mark-blush: #efc7c0;
  }
  * { margin: 0; padding: 0; box-sizing: border-box; }
  html, body { width: 1200px; height: 1200px; overflow: hidden; }
  body {
    background: var(--backdrop);
    font-family: "Barlow Semi Condensed", sans-serif;
    font-weight: 300;
    color: var(--type-light);
    position: relative;
  }

  /* Bottle */
  .bottle-cap {
    position: absolute;
    left: 409px; top: 230px; width: 132px; height: 160px;
    background: var(--cap-clear);
    border: 1px solid var(--cap-edge);
    border-radius: 8px 8px 0 0;
  }
  .pump-head { position: absolute; left: 436px; top: 250px; }
  .bottle-collar {
    position: absolute;
    left: 400px; top: 383px; width: 155px; height: 56px;
    background: var(--pack-white);
    border: 1px solid var(--pack-edge);
    border-radius: 10px 10px 0 0;
  }
  .bottle-body {
    position: absolute;
    left: 400px; top: 438px; width: 155px; height: 637px;
    background: var(--pack-white);
    border: 1px solid var(--pack-edge);
    border-top: none;
    border-radius: 0 0 8px 8px;
  }

  /* Carton */
  .carton {
    position: absolute;
    left: 619px; top: 182px; width: 234px; height: 890px;
    background: var(--pack-white);
    border: 1px solid var(--pack-edge);
  }

  .label {
    position: absolute;
    background: var(--label-sage);
    overflow: hidden;
    text-align: center;
  }
  .bottle-label { left: 417px; top: 447px; width: 119px; height: 620px; border-radius: 9px; }
  .carton-label { left: 632px; top: 196px; width: 213px; height: 857px; border-radius: 11px; }

  .leaf-art {
    position: absolute;
    border-radius: 50% 50% 40% 40% / 20% 20% 12% 12%;
    background: radial-gradient(ellipse at 55% 50%, rgba(205,214,189,0.95) 0%, rgba(205,214,189,0.6) 45%, rgba(205,214,189,0) 75%);
  }
  .bottle-label .leaf-art { left: 6px; right: 2px; top: 40px; height: 450px; }
  .carton-label .leaf-art { left: 4px; right: 0; top: 30px; height: 730px; }

  .title-block {
    position: absolute;
    background: var(--block-sage);
    border-radius: 6px;
  }
  .bottle-label .title-block { left: 2px; right: 2px; top: 200px; height: 159px; }
  .carton-label .title-block { left: 20px; right: 25px; top: 296px; height: 213px; }

  .title-block > div { position: absolute; left: 0; right: 0; }
  .brand-name { font-weight: 400; letter-spacing: 0.12em; line-height: 1; }
  .product-name { text-transform: uppercase; }
  .scent { text-transform: uppercase; line-height: 1; }

  .bottle-label .brand-name { top: 25px; font-size: 17px; }
  .bottle-label .product-name { top: 62px; font-size: 14.5px; line-height: 16px; }
  .bottle-label .scent { top: 140px; font-size: 10px; }

  .carton-label .brand-name { top: 26px; font-size: 24px; }
  .carton-label .product-name { top: 88px; font-size: 19px; line-height: 20.5px; }
  .carton-label .scent { top: 190px; font-size: 13px; }

  .brand-mark {
    position: absolute;
    left: 50%;
    transform: translateX(-50%);
    border-radius: 50%;
    background: var(--mark-blush);
    border: 2px solid var(--pack-white);
  }
  .bottle-label .brand-mark { top: 178px; width: 37px; height: 37px; }
  .carton-label .brand-mark { top: 270px; width: 47px; height: 47px; }

  .test-badge {
    position: absolute;
    left: 50%;
    transform: translateX(-50%);
    border-radius: 50%;
    background: var(--badge-tone);
  }
  .bottle-label .test-badge { top: 514px; width: 40px; height: 40px; }
  .carton-label .test-badge { top: 763px; width: 50px; height: 50px; }

  .volume-band {
    position: absolute;
    left: 0; right: 0; bottom: 0;
    background: var(--block-sage);
  }
  .bottle-label .volume-band { height: 67px; line-height: 67px; font-size: 11px; }
  .carton-label .volume-band { height: 59px; line-height: 59px; font-size: 14px; }
</style>
</head>
<body>
  <div class="bottle-cap"></div>
  <svg class="pump-head" width="80" height="135" viewBox="0 0 80 135" aria-hidden="true">
    <path d="M14 135 V70 Q14 52 30 44 L58 30 Q62 20 66 10 L74 10 L74 24 L64 26 V135 Z" fill="#cfdcc4"/>
    <rect x="10" y="92" width="60" height="5" fill="#c3d1b8"/>
    <rect x="8" y="115" width="64" height="5" fill="#c3d1b8"/>
  </svg>
  <div class="bottle-collar"></div>
  <div class="bottle-body"></div>

  <div class="carton"></div>

  <div class="label bottle-label">
    <div class="leaf-art" role="img" aria-label="Fine line drawing of climbing leafy stems"></div>
    <div class="title-block">
      <div class="brand-name">VELORIQUE</div>
      <div class="product-name">Light<br>Moisturising<br>Cream</div>
      <div class="scent">Citrus &amp; Green Tea</div>
    </div>
    <div class="brand-mark"></div>
    <div class="test-badge"></div>
    <div class="volume-band">50ml / 1.7 Fl. Oz.</div>
  </div>

  <div class="label carton-label">
    <div class="leaf-art" role="img" aria-label="Fine line drawing of climbing leafy stems"></div>
    <div class="title-block">
      <div class="brand-name">VELORIQUE</div>
      <div class="product-name">Light<br>Moisturising<br>Cream</div>
      <div class="scent">Citrus &amp; Green Tea</div>
    </div>
    <div class="brand-mark"></div>
    <div class="test-badge"></div>
    <div class="volume-band">50ml / 1.7 Fl. Oz.</div>
  </div>
</body>
</html>
```